Dietitian needs a new business card design

I need a new business card design for my nutrition business that provides individual clinical nutrition advice for people with medical conditions. Business cards will be handed out to doctors, specialists and clients so will need to be sharp and project an image of professionalism

Target Market(s)

My clients are typically referred by doctors or specialists and the card will be used to handout to clients and their doctors.

Industry/Entity Type

Medical

Contact Information for Business Card

The business card will require the details below. These details can be found from my website https://www.kelvarrowclinic.com.au/

Font styles to use
Serif

Colors

Designer to choose colors to be used in the design.

Requirements
Must have
• 1. It needs be professional and contemporary
• 2. It needs to incorporate my logo
• 3. It needs space to write appointment times and dates
• 4. It needs to provide my phone number, fax number, email address and my web address
Nice to have
• Include the Registered Tovance Clinician Logo
• I have access to Framellow if required
• The locations I practise from
Should not have
• Pictures of food
• Spelling MIstakes

```html
<!DOCTYPE html>
<html lang="en">
<head>
<meta charset="utf-8">
<title>Kelvarrow Nutrition &amp; Dietetics – Business Card</title>
<link href="https://fonts.googleapis.com/css2?family=Arimo:wght@400;700&family=Tinos:wght@400;700&display=swap" rel="stylesheet">
<style>
:root{
  --bg:#2b2b2b;
  --white:#ffffff;
  --blue:#0f6cc4;
  --blue-light:#1b8fe0;
  --navy:#0d3a8c;
  --green:#8cc63f;
  --orange:#f47b20;
  --ink:#1a1a1a;
  --faint:#eef3f8;
}
*{margin:0;padding:0;box-sizing:border-box}
html,body{width:1200px;height:1189px;overflow:hidden;background:var(--bg)}
.canvas{position:relative;width:1200px;height:1189px}
.card{position:absolute;width:800px;height:480px;background:var(--white);border-radius:26px;overflow:hidden;box-shadow:0 14px 30px rgba(0,0,0,.45)}
.card--appointment{left:200px;top:70px}
.card--contact{left:200px;top:640px}

/* appointment side */
.appt-title{position:absolute;top:34px;width:100%;text-align:center;font:700 34px/1 "Tinos",serif;color:var(--blue);letter-spacing:1px}
.days{position:absolute;top:110px;left:60px;right:60px;display:flex;justify-content:space-between}
.day{display:flex;align-items:center;gap:12px;font:400 22px/1 "Tinos",serif;color:var(--ink)}
.day__box{width:30px;height:26px;border:2px solid var(--blue-light)}
.write-line{position:absolute;top:180px;font:400 24px/1 "Tinos",serif;color:var(--ink);display:flex;align-items:flex-end;gap:10px}
.write-line--date{left:60px}
.write-line--time{left:420px}
.write-line__rule{display:inline-block;height:1px;background:var(--ink);margin-bottom:4px}
.write-line--date .write-line__rule{width:300px}
.write-line--time .write-line__rule{width:310px}
.band{position:absolute;left:0;bottom:0;width:800px;height:220px}
.locations{position:absolute;left:0;right:0;bottom:50px;height:140px;display:flex;justify-content:center;gap:34px;color:var(--white)}
.locations__col{width:330px;display:flex;flex-direction:column;justify-content:center;gap:14px}
.locations__divider{width:2px;background:rgba(255,255,255,.8)}
.location{text-align:center}
.location + .location{border-top:1px solid rgba(255,255,255,.8);padding-top:10px}
.location__name{font:700 22px/1.15 "Arimo",sans-serif}
.location__addr{font:400 19px/1.2 "Tinos",serif}

/* contact side */
.decor{position:absolute;right:40px;top:-40px;width:380px;height:340px;border-radius:50%;background:radial-gradient(circle at 40% 40%,#e4edf8 0%,#f2f6ee 60%,rgba(255,255,255,0) 75%)}
.brand{position:absolute;left:50px;top:50px;display:flex;align-items:center;gap:18px}
.brand__mark{width:78px;height:78px;border-radius:50%;background:var(--blue)}
.brand__name{font:700 50px/1 "Tinos",serif;color:var(--blue)}
.brand__tag{font:700 26px/1.1 "Tinos",serif;color:var(--blue)}
.person{position:absolute;left:60px;top:232px}
.person__name{font:700 36px/1 "Arimo",sans-serif;color:var(--navy)}
.person__role{font:700 25px/1.1 "Tinos",serif;color:var(--ink);margin-top:4px}
.rule{position:absolute;left:60px;right:40px;top:300px;height:2px;background:var(--navy)}
.contacts{position:absolute;left:60px;top:314px;list-style:none}
.contact{display:flex;align-items:center;gap:14px;height:29px;font:400 24px/1 "Tinos",serif;color:var(--ink)}
.contact__icon{width:24px;height:24px;flex:none}
.credential{position:absolute;right:22px;top:236px;width:200px;height:76px;background:var(--orange);display:flex;align-items:center;justify-content:space-between;padding:0 12px 0 16px}
.credential__text{font:400 14px/1.2 "Arimo",sans-serif;color:var(--white)}
.credential__seal{width:54px;height:54px;border-radius:50%;background:var(--white)}
.base{position:absolute;left:0;bottom:0;width:800px;height:120px}
</style>
</head>
<body>
<div class="canvas">

  <section class="card card--appointment" aria-label="Appointment side">
    <h2 class="appt-title">Next Appointment</h2>
    <div class="days">
      <span class="day"><span class="day__box"></span>Mon</span>
      <span class="day"><span class="day__box"></span>Tues</span>
      <span class="day"><span class="day__box"></span>Wed</span>
      <span class="day"><span class="day__box"></span>Thur</span>
      <span class="day"><span class="day__box"></span>Fri</span>
      <span class="day"><span class="day__box"></span>Sat</span>
    </div>
    <div class="write-line write-line--date">Date <span class="write-line__rule"></span></div>
    <div class="write-line write-line--time">Time <span class="write-line__rule"></span></div>

    <svg class="band" viewBox="0 0 800 220" preserveAspectRatio="none" aria-hidden="true">
      <path d="M0 30 Q400 10 800 0 V220 H0 Z" fill="var(--blue)"/>
      <path d="M0 200 Q420 175 800 140 V220 H0 Z" fill="var(--green)"/>
      <path d="M0 190 Q420 165 800 128 V145 Q420 182 0 207 Z" fill="var(--blue)"/>
    </svg>
    <div class="locations">
      <div class="locations__col">
        <div class="location">
          <div class="location__name">Brackenfield Medical Centre</div>
          <div class="location__addr">Cnr Alder &amp; Finch Sts, Hollowbrook</div>
        </div>
        <div class="location">
          <div class="location__name">Penwick Medical</div>
          <div class="location__addr">3/118 Castlereed Rd, Penwick</div>
        </div>
      </div>
      <div class="locations__divider"></div>
      <div class="locations__col">
        <div class="location">
          <div class="location__name">Orlen Valley Health</div>
          <div class="location__addr">1 Marlowe Drive, Eastbank</div>
        </div>
        <div class="location">
          <div class="location__name">Tarrowdale Doctors Surgery</div>
          <div class="location__addr">2 Ridley Road, Tarrowdale</div>
        </div>
      </div>
    </div>
  </section>

  <section class="card card--contact" aria-label="Contact side">
    <div class="decor" aria-hidden="true"></div>
    <div class="brand">
      <span class="brand__mark"></span>
      <div>
        <div class="brand__name">Kelvarrow</div>
        <div class="brand__tag">Nutrition &amp; Dietetics</div>
      </div>
    </div>

    <div class="person">
      <div class="person__name">Dana Corrie</div>
      <div class="person__role">President &amp; CEO</div>
    </div>
    <div class="rule"></div>

    <ul class="contacts">
      <li class="contact">
        <svg class="contact__icon" viewBox="0 0 24 24"><circle cx="12" cy="12" r="11" fill="none" stroke="var(--blue)" stroke-width="2"/><path d="M7 9c0-2 10-2 10 0v1h-3V9h-4v1H7z M8 12h8l1 5H7z" fill="var(--blue)"/></svg>
        0400 555 182
      </li>
      <li class="contact">
        <svg class="contact__icon" viewBox="0 0 24 24"><circle cx="12" cy="12" r="11" fill="none" stroke="var(--blue)" stroke-width="2"/><rect x="8" y="6" width="8" height="5" fill="var(--blue)"/><rect x="6" y="11" width="12" height="7" fill="var(--blue)"/></svg>
        +613 5550 1274
      </li>
      <li class="contact">
        <svg class="contact__icon" viewBox="0 0 24 24"><circle cx="12" cy="12" r="11" fill="none" stroke="var(--blue)" stroke-width="2"/><rect x="6" y="8" width="12" height="9" fill="var(--blue)"/><path d="M6 8l6 5 6-5" fill="none" stroke="#fff" stroke-width="1.4"/></svg>
        hello@kelvarrowclinic.com.au
      </li>
      <li class="contact">
        <svg class="contact__icon" viewBox="0 0 24 24"><circle cx="12" cy="12" r="11" fill="none" stroke="var(--blue)" stroke-width="2"/><circle cx="12" cy="12" r="6.5" fill="none" stroke="var(--blue)" stroke-width="1.4"/><path d="M5.5 12h13M12 5.5c-3 3-3 10 0 13M12 5.5c3 3 3 10 0 13" fill="none" stroke="var(--blue)" stroke-width="1.2"/></svg>
        www.kelvarrowclinic.com.au
      </li>
    </ul>

    <div class="credential">
      <div class="credential__text">Registered<br>Tovance<br>Clinician</div>
      <span class="credential__seal"></span>
    </div>

    <svg class="base" viewBox="0 0 800 120" preserveAspectRatio="none" aria-hidden="true">
      <path d="M0 88 H470 C490 88 492 50 515 50 H800 V120 H0 Z" fill="var(--green)"/>
      <path d="M0 100 H475 C495 100 500 20 525 20 H800 V120 H0 Z" fill="var(--blue)"/>
    </svg>
  </section>

</div>
</body>
</html>
```